Create an awesome website for a medical clinic

This is a new website for a doctor's office. The site should be clean and modern, easy to navigate.

This is a wellness clinic, we want to help our clients have a healthy, active lifestyle. It should be friendly and inviting, and easy for them to call or schedule an appointment.

The site should be responsive and designed using the attached Bootstrap 3 PSD.

We will provide stock photos, until then please use stock photos from:

pictovault.net or
imagebarrow.net (preferred)

Some example sites of clean and modern designs that we like:

https://tarvelspine.example/
http://quellmarrow.example/
http://brisklyhale.example/

Also attached is a temporary logo you can use.

Reason: Thank you everyone for your great designs - we need a little more time so I'm extending the project.

Need extra days to review

Also, the colors in the new logo I just linked to are the final colors of the logo, so feel free to use any complimentary colors to it.

Hi everyone, The boss wants to change the layout of the site a little bit - here's the revised layout: https://www.filecrate.example/s/k9pz31xq7vn84te/notes%2011_29_2017.pdf?dl=0 And the graphic assets you can use are here: https://www.filecrate.example/s/k9pz31xq7vn84te/notes%2011_29_2017.pdf?dl=0 Feel free to change the background color of the "topbar", and change the icons of the "why people trust us" if you want, these are just temporary placeholders. Thanks for your patience and hard work!

Target Market(s)

People seeking medical treatment (wellness clinic)

Industry/Entity Type

Doctor

Number of Pages Required

1 page

Font styles to use
Sans Serif

Colors
0592cd
33a6d7
abd037
9bcb3c

Requirements
Must have
• The home page should have: a strong hero image/slideshow, clinic phone number should be prominent and at the top of the page (in the nav), a "what to expect" section (this is like a FAQs section - see attachment), and a strong call to action (a button to call or schedule an appointment).
• The what to expect section is useful so that prospective clients can determine if we're a good fit for them or not. It's a basic, first-step pre-qualification block of information.
• Social media icons which links to our social media profiles should be included.
Nice to have
• - Link to 3 most recent blog entries
• - Testimonials
• - How a multilevel nav menu looks.

```html
<!DOCTYPE html>
<html lang="en">
<head>
<meta charset="utf-8">
<title>Verdale Medical Clinic</title>
<link href="https://fonts.googleapis.com/css2?family=Lato:wght@300;400;700;900&family=Roboto:wght@400;500;700&display=swap" rel="stylesheet">
<style>
:root{
  --green:#8dc63f;
  --green-light:#abd037;
  --green-mid:#9bcb3c;
  --blue:#0592cd;
  --blue-light:#33a6d7;
  --teal:#1fa59a;
  --ink:#333;
  --grey:#777;
  --pale-blue:#e8f4f8;
  --pale-grey:#f2f2f2;
  --white:#fff;
}
*{box-sizing:border-box;margin:0;padding:0}
html,body{width:1200px;height:3846px;overflow:hidden;background:var(--white)}
body{position:relative;font-family:'Lato',sans-serif;color:var(--ink)}
.abs{position:absolute}
/* header */
.logo{left:59px;top:22px;color:var(--green);font-weight:900;line-height:1}
.logo .name{font-size:36px;letter-spacing:1px}
.logo .sub{font-size:12px;letter-spacing:1.5px;margin-top:4px}
.contact{top:32px;display:flex;align-items:center;gap:10px;font-size:10px;color:var(--ink);white-space:nowrap}
.contact .ico{width:34px;height:34px;border:1px solid #ddd;border-radius:50%;display:flex;align-items:center;justify-content:center;flex:none}
.contact b{display:block;font-size:10px}
.btn-appoint{left:918px;top:31px;width:223px;height:46px;background:var(--green);color:var(--white);font-weight:700;font-size:17px;display:flex;align-items:center;justify-content:center;gap:10px}
/* nav */
.nav{left:59px;top:102px;width:1082px;height:67px;background:linear-gradient(90deg,#7fc04b,#58b860 60%,#6cc04c);border-bottom:4px solid var(--blue-light);font-family:'Roboto',sans-serif;font-size:16px;color:var(--white)}
.nav a{position:absolute;top:0;height:63px;line-height:63px;color:var(--white);text-decoration:none;transform:translateX(-50%)}
.nav .active{background:var(--green-light);width:128px;text-align:center;transform:none}
/* hero */
.hero-photo{left:59px;top:169px;width:485px;height:469px;background:linear-gradient(135deg,#dfe9ee,#c9dbe3 60%,#b7d0a8)}
.hero-panel{left:544px;top:169px;width:597px;height:469px;background:linear-gradient(135deg,#4fbf7a,#1aa3a6 40%,#0a8fcf)}
.hero-panel h1{position:absolute;left:66px;top:104px;font-family:'Roboto',sans-serif;font-size:31px;font-weight:500;color:var(--white);line-height:1.25;width:440px}
.hero-panel p{position:absolute;left:66px;top:186px;width:440px;font-size:16px;line-height:1.3;color:var(--white)}
.hero-panel hr{position:absolute;left:66px;top:270px;width:455px;border:0;border-top:1px solid rgba(255,255,255,.7)}
.btn-outline{border:2px solid var(--white);color:var(--white);font-weight:700;text-align:center}
.hero-panel .btn-outline{position:absolute;left:66px;top:286px;width:196px;height:48px;line-height:44px;font-size:15px}
/* service strip */
.strip{top:638px;width:361px;height:249px;color:var(--white);padding:34px 36px}
.strip h3{font-size:20px;font-weight:400;margin-bottom:18px}
.strip p{font-size:13px;line-height:1.5}
.strip .more{display:inline-block;margin-top:22px;border:1px solid var(--white);font-size:12px;padding:8px 12px}
.strip .row{display:flex;justify-content:space-between;font-size:13px;padding:12px 0;border-bottom:1px solid rgba(255,255,255,.5)}
/* section titles */
.center{text-align:center;left:0;width:1200px}
.title-lg{font-size:46px;color:var(--green);font-weight:300}
.title-lg b{font-weight:700}
.lead{font-size:19px;color:var(--grey);line-height:1.6}
.rule{width:180px;height:2px;background:var(--blue-light);left:510px}
/* features */
.intro{left:0;top:887px;width:1200px;height:600px;background:var(--pale-blue)}
.feature{top:1175px;width:260px;text-align:center}
.feature .ring{width:164px;height:164px;border-radius:50%;border:3px solid var(--teal);margin:0 auto;display:flex;align-items:center;justify-content:center}
.feature p{margin-top:26px;font-size:20px;line-height:1.5;color:var(--ink)}
/* about */
.about{left:0;top:1487px;width:1200px;height:518px;background:var(--pale-grey)}
.h-split{font-size:40px;font-weight:700}
.h-split .g{color:var(--green)}.h-split .b{color:var(--blue)}
.about-photo{left:730px;top:1512px;width:411px;height:488px;background:linear-gradient(180deg,#f3f3f3,#e4ecef 50%,#d6eaf0)}
.stat{top:1853px;width:290px;height:97px;background:var(--white);border:2px solid #ddd;display:flex;align-items:center;gap:18px;padding-left:26px}
.stat b{display:block;color:var(--green);font-size:20px;font-weight:400}
.stat span{font-size:15px;color:var(--ink)}
/* blogs */
.blog-cell{width:300px;height:169px}
.blog-photo{background:linear-gradient(135deg,#e6eef1,#cddde4)}
.blog-text{background:#f6f6f6;padding:46px 20px 0 24px}
.blog-text h4{font-size:15px;font-weight:400;margin-bottom:8px;padding-left:64px}
.blog-text p{font-size:10.5px;line-height:1.35;color:var(--grey);padding-left:64px}
.blog-text svg{position:absolute;left:24px;top:54px}
.arrow{width:38px;height:38px;border-radius:50%;background:var(--white);border:1px solid #ddd;display:flex;align-items:center;justify-content:center}
.sub-text{left:320px;width:560px;text-align:center;font-size:16px;line-height:1.6;color:#444}
/* doctors */
.doctors{left:0;top:2564px;width:1200px;height:590px;background:#ebebeb}
.doc{top:2764px;width:249px;height:303px;background:var(--white)}
.doc .ph{height:226px;background:linear-gradient(180deg,#eef3f5,#d5e3ea)}
.doc p{text-align:center;color:var(--green-mid);font-weight:700;font-size:18px;line-height:77px}
.dot{top:3116px;width:11px;height:11px;border-radius:50%;background:#b8d7dc}
/* testimonials */
.testi{left:0;top:3154px;width:1200px;height:551px;background:linear-gradient(120deg,#2aa4dc 0%,#3ab0b8 45%,#9ccd3a 100%)}
.card{top:3338px;width:326px;height:247px;border:2px solid rgba(255,255,255,.85);color:var(--white);padding:92px 26px 0;font-size:14px;line-height:1.35}
.card .who{margin-top:20px;font-size:14px}
.avatar{top:3278px;width:110px;height:110px;border-radius:50%;border:4px solid rgba(255,255,255,.9);background:linear-gradient(135deg,#e9eef0,#c8d4da)}
/* footer */
.footer{left:0;top:3718px;width:1200px;height:128px;background:var(--green);text-align:center;line-height:128px;font-size:16px;color:#222}
</style>
</head>
<body>

<!-- header -->
<div class="abs logo"><div class="name">VERDALE</div><div class="sub">MEDICAL CLINIC</div></div>
<div class="abs contact" style="left:610px">
  <div class="ico"><svg width="16" height="16" viewBox="0 0 24 24"><path d="M6.6 10.8a15 15 0 0 0 6.6 6.6l2.2-2.2a1 1 0 0 1 1-.25 11 11 0 0 0 3.6.57 1 1 0 0 1 1 1V20a1 1 0 0 1-1 1A17 17 0 0 1 3 4a1 1 0 0 1 1-1h3.5a1 1 0 0 1 1 1c0 1.25.2 2.45.57 3.57a1 1 0 0 1-.25 1z" fill="#333"/></svg></div>
  <div><b>Call Us</b>(555) 014 2290</div>
</div>
<div class="abs contact" style="left:760px">
  <div class="ico"><svg width="16" height="16" viewBox="0 0 24 24"><rect x="3" y="5" width="18" height="14" rx="1" fill="none" stroke="#333" stroke-width="2"/><path d="M3 6l9 7 9-7" fill="none" stroke="#333" stroke-width="2"/></svg></div>
  <div><b>Email Us</b>info@verdale.example</div>
</div>
<div class="abs btn-appoint"><svg width="20" height="20" viewBox="0 0 24 24"><circle cx="12" cy="8" r="4" fill="#fff"/><path d="M4 21c0-4.4 3.6-7 8-7s8 2.6 8 7z" fill="#fff"/></svg>Get Appointment</div>

<!-- nav -->
<nav class="abs nav">
  <a class="active" style="left:87px">Home</a>
  <a style="left:320px">About Us</a>
  <a style="left:474px">Our Patients</a>
  <a style="left:666px">Our Treatments</a>
  <a style="left:838px">Galliers</a>
  <a style="left:984px">Contact Us</a>
</nav>

<!-- hero -->
<div class="abs hero-photo" role="img" aria-label="Smiling dentist standing beside a patient in a treatment chair"></div>
<div class="abs hero-panel">
  <h1>It is a long established fact by readable content</h1>
  <p>There are many variations of passages of Lorem Ipsum available, but the majority have suffered alteration in some form, by injected humour,</p>
  <hr>
  <div class="btn-outline">ALTERATION</div>
</div>

<!-- strip -->
<div class="abs strip" style="left:59px;background:#1590cc">
  <h3>Aublishing software</h3>
  <p>The generated Lorem Ipsum is therefore always free from repetition, injected humour, or non-characteristic.</p>
  <span class="more">Read more</span>
</div>
<div class="abs strip" style="left:420px;background:#15999e">
  <h3>Publishing software</h3>
  <p>The generated Lorem Ipsum is therefore always free from repetition, injected humour, or non-characteristic.</p>
  <span class="more">Read more</span>
</div>
<div class="abs strip" style="left:780px;background:var(--green-mid);padding-top:34px">
  <h3 style="margin-bottom:8px">Publishing software</h3>
  <div class="row"><span>Carlopng - Criond</span><span>09.00 - 16.00</span></div>
  <div class="row"><span>Carlopngy</span><span>09.30 - 16.00</span></div>
  <div class="row" style="border:0"><span>Carlopngy</span><span>09.30 - 15.00</span></div>
</div>

<!-- intro / features -->
<section class="abs intro"></section>
<h2 class="abs center title-lg" style="top:945px">We are in <b>Lorem Ipsum...</b></h2>
<p class="abs lead" style="left:290px;top:1020px;width:620px;text-align:center">Randomised words which don't look even slightly believable. If you are going to use a passage of Lorem Ipsum, you need to be sure there</p>
<div class="abs rule" style="top:1104px"></div>

<div class="abs feature" style="left:96px">
  <div class="ring"><svg width="70" height="70" viewBox="0 0 64 64" fill="none" stroke="#1fa59a" stroke-width="2.5"><rect x="24" y="6" width="16" height="8"/><rect x="16" y="14" width="32" height="44" rx="3"/><path d="M32 28v16M24 36h16"/></svg></div>
  <p>Randomised words<br>which don't.</p>
</div>
<div class="abs feature" style="left:352px">
  <div class="ring"><svg width="70" height="70" viewBox="0 0 64 64" fill="none" stroke="#1fa59a" stroke-width="2.5"><path d="M22 4c0 20 20 20 20 28S22 40 22 60M42 4c0 20-20 20-20 28s20 8 20 28"/><path d="M26 12h12M24 20h16M24 44h16M26 52h12"/></svg></div>
  <p>Randomised words<br>which don't look.</p>
</div>
<div class="abs feature" style="left:626px">
  <div class="ring"><svg width="70" height="70" viewBox="0 0 64 64" fill="none" stroke="#1fa59a" stroke-width="2.5"><path d="M30 8l8 4-10 20-8-4z"/><path d="M24 36a14 14 0 0 0 22 12"/><path d="M14 56h36M32 48v8"/><circle cx="22" cy="34" r="3"/></svg></div>
  <p>Randomised words<br>which don't.</p>
</div>
<div class="abs feature" style="left:883px">
  <div class="ring"><svg width="70" height="70" viewBox="0 0 64 64" fill="none" stroke="#1fa59a" stroke-width="2.5"><path d="M30 8l8 4-10 20-8-4z"/><path d="M24 36a14 14 0 0 0 22 12"/><path d="M14 56h36M32 48v8"/><circle cx="22" cy="34" r="3"/></svg></div>
  <p>Randomised words<br>which don't.</p>
</div>

<!-- about -->
<section class="abs about"></section>
<h2 class="abs h-split" style="left:105px;top:1520px"><span class="g">Verdale</span> <span class="b">About...</span></h2>
<p class="abs" style="left:105px;top:1580px;width:600px;font-size:16px;font-weight:700;line-height:1.45;color:#222">Lorem ipsum will uncover many web <span style="font-weight:400">There are many variations of passagesof Lorem ipsum available, but the majority.sites still.</span></p>
<div class="abs" style="left:105px;top:1650px;width:110px;height:2px;background:var(--blue-light)"></div>
<p class="abs" style="left:105px;top:1672px;width:600px;font-size:18px;line-height:1.6;color:var(--grey)">There are many variations of passages of Lorem ipsum available, but the majority.There are many variations of passages of Lorem ipsum available, but the majority.There are many variations of passages of Loremipsum available, but the majority.</p>
<div class="abs stat" style="left:105px">
  <svg width="44" height="50" viewBox="0 0 44 50" fill="none" stroke="#1fa59a" stroke-width="2.5"><path d="M22 4v44M14 12h16"/><path d="M30 20c-10 0-16 6-8 10s2 10-6 10"/></svg>
  <div><b>20 years</b><span>oremipsum available</span></div>
</div>
<div class="abs stat" style="left:423px">
  <svg width="46" height="46" viewBox="0 0 46 46" fill="none" stroke="#1fa59a" stroke-width="2.5"><path d="M17 4h12v13h13v12H29v13H17V29H4V17h13z"/></svg>
  <div><b>45 years</b><span>oremipsum available</span></div>
</div>
<div class="abs about-photo" role="img" aria-label="Female doctor with stethoscope, arms folded"></div>

<!-- blogs -->
<h2 class="abs center" style="top:2044px;font-size:26px;font-weight:700"><span style="color:var(--green)">Recent</span> <span style="color:var(--blue)">Blogs</span></h2>
<p class="abs sub-text" style="top:2090px">Lorem ipsum will uncover many web There are many variations of passagesof Lorem but the majority.sites still.</p>
<div class="abs rule" style="left:555px;width:90px;top:2160px"></div>

<div class="abs blog-cell blog-photo" style="left:0;top:2205px" role="img" aria-label="Doctor talking with a patient"></div>
<div class="abs blog-cell blog-text" style="left:300px;top:2205px">
  <svg width="40" height="34" viewBox="0 0 40 34" fill="none" stroke="#1fa59a" stroke-width="2"><path d="M20 32S2 20 2 10a9 9 0 0 1 18-3 9 9 0 0 1 18 3c0 10-18 22-18 22z"/><path d="M6 17h8l3-6 4 11 3-5h10"/></svg>
  <h4>Verdale Services</h4><p>Lorem ipsum will uncover many web there are many variations of passage of Lorem but the majority sites still.</p>
</div>
<div class="abs blog-cell blog-photo" style="left:600px;top:2205px" role="img" aria-label="Hands taking a blood sample from a fingertip"></div>
<div class="abs blog-cell blog-text" style="left:900px;top:2205px">
  <svg width="40" height="34" viewBox="0 0 40 34" fill="none" stroke="#1fa59a" stroke-width="2"><rect x="2" y="8" width="36" height="24" rx="2"/><path d="M14 8V3h12v5M20 13v14M13 20h14"/></svg>
  <h4>Verdale Services</h4><p>Lorem ipsum will uncover many web there are many variations of passage of Lorem but the majority sites still.</p>
</div>
<div class="abs blog-cell blog-text" style="left:0;top:2374px">
  <svg width="34" height="40" viewBox="0 0 34 40" fill="none" stroke="#1fa59a" stroke-width="2"><rect x="3" y="5" width="28" height="33" rx="2"/><path d="M11 5V2h12v3M10 16l4 4 8-8M10 28h14"/></svg>
  <h4>Verdale Services</h4><p>Lorem ipsum will uncover many web there are many variations of passage of Lorem but the majority sites still.</p>
</div>
<div class="abs blog-cell blog-photo" style="left:300px;top:2374px" role="img" aria-label="Doctor examining a child at an eye chart"></div>
<div class="abs blog-cell blog-text" style="left:600px;top:2374px">
  <svg width="40" height="34" viewBox="0 0 40 34" fill="none" stroke="#1fa59a" stroke-width="2"><path d="M4 16a16 12 0 0 1 32 0z"/><path d="M2 16h36M6 22h28M8 28h24"/></svg>
  <h4>Verdale Services</h4><p>Lorem ipsum will uncover many web there are many variations of passage of Lorem but the majority sites still.</p>
</div>
<div class="abs blog-cell blog-photo" style="left:900px;top:2374px" role="img" aria-label="Doctor reviewing notes with a young patient"></div>
<div class="abs arrow" style="left:22px;top:2353px"><svg width="12" height="12" viewBox="0 0 12 12"><path d="M8 1L3 6l5 5" fill="none" stroke="#666" stroke-width="2"/></svg></div>
<div class="abs arrow" style="left:1140px;top:2353px"><svg width="12" height="12" viewBox="0 0 12 12"><path d="M4 1l5 5-5 5" fill="none" stroke="#666" stroke-width="2"/></svg></div>

<!-- doctors -->
<section class="abs doctors"></section>
<h2 class="abs center" style="top:2590px;font-size:26px;font-weight:700"><span style="color:var(--green)">Verdale</span> <span style="color:var(--blue)">Doctors</span></h2>
<p class="abs sub-text" style="top:2634px">Lorem ipsum will uncover many web There are many variations of passagesof Lorem but the majority.sites still.</p>
<div class="abs rule" style="left:555px;width:90px;top:2706px"></div>
<div class="abs doc" style="left:225px"><div class="ph" role="img" aria-label="Portrait of a senior male doctor"></div><p>Verdale Doctors</p></div>
<div class="abs doc" style="left:520px"><div class="ph" role="img" aria-label="Portrait of a female doctor"></div><p>Verdale Doctors</p></div>
<div class="abs doc" style="left:813px"><div class="ph" role="img" aria-label="Portrait of a female doctor"></div><p>Verdale Doctors</p></div>
<div class="abs dot" style="left:614px;background:#6aaab8"></div>
<div class="abs dot" style="left:631px"></div>
<div class="abs dot" style="left:648px"></div>

<!-- testimonials -->
<section class="abs testi"></section>
<h2 class="abs center" style="top:3184px;font-size:40px;font-weight:700;color:var(--white)">What Patients say...</h2>
<div class="abs card" style="left:72px">It uses a dictionary of over 200 Latin words, combined with a handful of model sentence structures, to genere Lorem Ipsum<div class="who"><b>Adrome.</b><br>Patient</div></div>
<div class="abs card" style="left:443px">It uses a dictionary of over 200 Latin words, combined with a handful of model sentence structures, to genere Lorem Ipsum<div class="who"><b>Adrome.</b><br>Patient</div></div>
<div class="abs card" style="left:815px">It uses a dictionary of over 200 Latin words, combined with a handful of model sentence structures, to genere Lorem Ipsum<div class="who"><b>Adrome.</b><br>Patient</div></div>
<div class="abs avatar" style="left:180px" role="img" aria-label="Patient portrait"></div>
<div class="abs avatar" style="left:551px" role="img" aria-label="Patient portrait"></div>
<div class="abs avatar" style="left:923px" role="img" aria-label="Patient portrait"></div>

<!-- footer -->
<footer class="abs footer">Copyrightverdalemedical@2017.All rights are reserved</footer>

</body>
</html>
```